Morrow & Pellant Stationery

Greetings again. Now we've got an awesome logo, it's time to get the stationery to go with it. We require the following items of stationery:

- Business Card - Print Ready, all we need to do is change names and numbers and submit to printer.  Double sided with logo on one side and details on the other side. (85mm x 55mm)

- With Compliments Slip

- Letterhead - These will be preprinted pages that will then be used as pages.
(A4)

- Envelope - Business Size(Standard DL)

Target Market(s)

Essentially, this firm services clients facing criminal charges and/or seeking legal aid. The firm is also looking at taking on more white-collar crime cases.

Requirements
Must have
• - Same Design Cues & Colours as the Branding details attached

• - Address (as follows)

• Suite 8

• 212-216 Carrow St

• ASHCOMBE VIC 3190

• Phone: (03) 9555 0142

• Fax: (03) 9555 0187

• Web: www.morrowandpellant.example

• - Colour: Pantone 194 (Red)

```html
<!DOCTYPE html>
<html lang="en">
<head>
<meta charset="utf-8">
<title>Morrow &amp; Pellant Stationery</title>
<link rel="stylesheet" href="https://fonts.googleapis.com/css2?family=Cinzel:wght@400;600&display=swap">
<style>
  :root {
    --brand-red: #a30f3b;
    --backdrop: #6b6b6b;
    --paper: #ffffff;
    --ink: #3a3a3a;
    --soft-grey: #bfc0c2;
    --faint-grey: #d6d6d8;
    --frame-grey: #c8c9cb;
    --black: #111111;
  }
  * { box-sizing: border-box; margin: 0; padding: 0; }
  html, body { width: 1200px; height: 883px; overflow: hidden; }
  body {
    background: var(--backdrop);
    font-family: "Cinzel", "Times New Roman", serif;
    position: relative;
  }
  .item { position: absolute; }

  /* Brand lockup: plain circle + name */
  .lockup { display: flex; align-items: center; gap: 8px; }
  .lockup__dot { border-radius: 50%; flex: none; }
  .lockup__name, .lockup__tag {
    display: block; font-weight: 600; line-height: 1.05; white-space: nowrap;
  }

  /* Letterhead */
  .letterhead-backing {
    left: 245px; top: 20px; width: 572px; height: 845px;
    background: var(--brand-red);
  }
  .letterhead {
    left: 237px; top: 15px; width: 572px; height: 856px;
    background: var(--paper);
    border: 3px solid var(--frame-grey);
  }
  .letterhead .lockup { position: absolute; left: 130px; top: 740px; gap: 12px; }
  .letterhead .lockup__dot { width: 64px; height: 64px; background: var(--faint-grey); }
  .letterhead .lockup__name { font-size: 25px; color: var(--faint-grey); }
  .letterhead .lockup__tag { font-size: 18px; color: var(--faint-grey); margin-top: 3px; }
  .letterhead__footer {
    position: absolute; left: 0; right: 0; bottom: 6px;
    text-align: center; font-size: 6px; letter-spacing: 0.3px; color: var(--ink);
    white-space: nowrap;
  }

  /* Business card front */
  .card-front {
    left: 161px; top: 246px; width: 269px; height: 161px;
    background: var(--brand-red);
  }
  .card-front .lockup { position: absolute; left: 17px; top: 60px; }
  .card-front .lockup__dot { width: 40px; height: 40px; background: var(--paper); }
  .card-front .lockup__name { font-size: 18px; color: var(--paper); }
  .card-front .lockup__tag { font-size: 11.5px; color: var(--paper); margin-top: 2px; }

  /* Business card back */
  .card-back {
    left: 141px; top: 443px; width: 161px; height: 267px;
    background: var(--paper); overflow: hidden;
  }
  .card-back__bar { height: 26px; background: var(--black); }
  .card-back__details {
    position: relative; z-index: 1;
    text-align: center; padding-top: 8px; color: var(--ink);
  }
  .card-back__name { font-size: 11px; letter-spacing: 1.5px; }
  .card-back__line { font-size: 6.5px; letter-spacing: 0.4px; line-height: 1.35; }
  .card-back__email { font-size: 4.5px; margin-top: 3px; letter-spacing: 0.2px; }
  .card-back__disc {
    position: absolute; left: 30px; top: 95px; width: 102px; height: 102px;
    border-radius: 50%; background: var(--faint-grey);
  }
  .card-back .lockup { position: absolute; left: 10px; top: 205px; gap: 5px; }
  .card-back .lockup__dot { width: 22px; height: 22px; background: var(--brand-red); }
  .card-back .lockup__name { font-size: 9.5px; color: var(--ink); }
  .card-back .lockup__tag { font-size: 6.5px; color: var(--ink); margin-top: 1px; }
  .card-back__web {
    position: absolute; left: 0; right: 0; bottom: 0; height: 15px;
    background: var(--brand-red); color: var(--paper);
    font-size: 5.5px; letter-spacing: 0.6px; text-align: center; line-height: 15px;
  }

  /* Compliments slip reverse */
  .comp-slip {
    left: 680px; top: 180px; width: 266px; height: 163px;
    background: var(--soft-grey); border: 2px solid #e2e2e3;
  }
  .comp-slip svg { position: absolute; right: 0; bottom: 0; }

  /* Envelope */
  .envelope-shadow {
    left: 525px; top: 436px; width: 672px; height: 304px; background: #1e1e1e;
  }
  .envelope {
    left: 513px; top: 422px; width: 672px; height: 304px;
    background: var(--frame-grey); padding: 15px 18px;
  }
  .envelope__face { width: 100%; height: 100%; background: var(--paper); position: relative; }
  .envelope .lockup { position: absolute; left: 14px; top: 16px; }
  .envelope .lockup__dot { width: 36px; height: 36px; background: var(--brand-red); }
  .envelope .lockup__name { font-size: 15px; color: var(--ink); }
  .envelope .lockup__tag { font-size: 10px; color: var(--ink); margin-top: 1px; }
</style>
</head>
<body>
  <div class="item letterhead-backing"></div>
  <section class="item letterhead" aria-label="Letterhead">
    <div class="lockup">
      <span class="lockup__dot"></span>
      <div><span class="lockup__name">Morrow &amp; Pellant</span><span class="lockup__tag">Barristers &amp; Solicitors</span></div>
    </div>
    <p class="letterhead__footer">Suite 8, 212-216 Carrow St, Ashcombe VIC 3190 &nbsp;|&nbsp; P (03) 9555 0142 &nbsp;|&nbsp; F (03) 9555 0187 &nbsp;|&nbsp; info@morrowandpellant.example &nbsp;|&nbsp; www.morrowandpellant.example</p>
  </section>

  <section class="item card-front" aria-label="Business card front">
    <div class="lockup">
      <span class="lockup__dot"></span>
      <div><span class="lockup__name">Morrow &amp; Pellant</span><span class="lockup__tag">Barristers &amp; Solicitors</span></div>
    </div>
  </section>

  <section class="item card-back" aria-label="Business card back">
    <div class="card-back__bar"></div>
    <span class="card-back__disc"></span>
    <div class="card-back__details">
      <p class="card-back__name">Daniel Harrow</p>
      <p class="card-back__line">212-216 Carrow St, Suite 8</p>
      <p class="card-back__line">Ashcombe VIC 3190</p>
      <p class="card-back__line">P (03) 9555 0142</p>
      <p class="card-back__line">F (03) 9555 0187</p>
      <p class="card-back__email">info@morrowandpellant.example</p>
    </div>
    <div class="lockup">
      <span class="lockup__dot"></span>
      <div><span class="lockup__name">Morrow &amp; Pellant</span><span class="lockup__tag">Barristers &amp; Solicitors</span></div>
    </div>
    <p class="card-back__web">www.morrowandpellant.example</p>
  </section>

  <section class="item comp-slip" aria-label="With compliments slip">
    <svg width="20" height="20" viewBox="0 0 20 20"><polygon points="20,0 20,20 0,20" fill="#a30f3b"/></svg>
  </section>

  <div class="item envelope-shadow"></div>
  <section class="item envelope" aria-label="DL envelope">
    <div class="envelope__face">
      <div class="lockup">
        <span class="lockup__dot"></span>
        <div><span class="lockup__name">Morrow &amp; Pellant</span><span class="lockup__tag">Barristers &amp; Solicitors</span></div>
      </div>
    </div>
  </section>
</body>
</html>
```